QUORVIX - Sydney Based Technology Consultancy -Logo & Business Card design

Who are we?
-
Quorvix is an emerging and advanced technology consulting and professional services business based in Sydney, Australia. Quorvix specialising in increasing value to organisations through the effective use of current and emerging technologies, ensuring that technology is a sustainable catalyst to attaining stated business goals.

We pride ourselves in challenging the norm.

What do we want?
-
We are looking to update our "Brand" we already have a simple “home grown” logo and we are now looking for a new one, once we have this updated logo and businesses look and feel though the business card design we will refresh our website with the new logo and design thus updating the Companies overall look at feel.

Our current site is www.quorvix-example.net.au is a very basic wordpress site and we will be updating it once we have the new logo and designs done

Our initial thoughts on the new Quorvix identity are
• Logo Concept
- One of the key things is obviously the 8
- I was thinking that a logo that had 8 as the core of the logo would be cool,
- Almost like having a “ring” or hoop that is twisted to form an 8 with different services scribed on the inside.
- So we would have a Large 8 and the inside would have ring each service or section engraved.

• Brand / web Feel
- Simple
- Professional
- Innovative
- Clear
- Destination
- Unique
- Impartial
- Safe
- Leading edge
- Familiar

- Emerging technologies
- White and ice / glacier blue
- The familiar feel of the Brindle web site
- Embedded specialist Video clips

• Portfolio of Services
- Quorvix – A smart place for Smart people
- Quorvix – we provide the process to take ideas from awareness to reality
- Focus should be on the brand quality consistent clear local knowledge with regional, national, theatre and global presence

Access to Specialists
- Emerging technologies
- Sustainability
- Collaboration
- Data centre
- Virtualisation

• Adjacent ideas under the one Brand
- Tembrosk – Enable Business Collaboration
- Plinsk – Infrastructure Virtualisation
- morvo - smart people and processes
- skandel - Emerging technologies
- brunhavel - business to technology integration
- tolpin - Smart Infrastructure
- yusk – Connected communities
- dwol - sustainability

Target Market(s)

Australia, New Zealand and Asia pacific organisations that are typically English speaking.
Markets
- IT & Technology partners
- Banking and Finance
- Health

Industry/Entity Type

Business

Requirements
Must have
• Logo
Business cards
Colour pallette
3D Logo
Nice to have
• Style guide
Designer who can also assist with new Wordpress design
Should not have
• we don't want cheap looking, overtly flashy or gimmicky logo.

```html
<!DOCTYPE html>
<html lang="en">
<head>
<meta charset="utf-8">
<title>Quorvix – Stationery</title>
<link rel="stylesheet" href="https://fonts.googleapis.com/css2?family=Source+Sans+3:wght@400;600&display=swap">
<style>
  :root{
    --stage:#1f1f21;
    --glacier:#1ea3dc;
    --glacier-deep:#0b7fb4;
    --ice:#e9edf0;
    --ice-shade:#d3d9de;
    --slate:#4a4b4e;
    --slate-deep:#333436;
    --white:#ffffff;
    --ink:#3a3a3a;
    --font:"Source Sans 3", "Myriad Pro", Arial, sans-serif;
  }
  *{box-sizing:border-box;margin:0;padding:0}
  html,body{width:1200px;height:1007px;overflow:hidden}
  body{background:var(--stage);font-family:var(--font);position:relative}

  .wordmark{display:flex;align-items:center;gap:10px;font-weight:600;letter-spacing:.5px;white-space:nowrap}
  .wordmark .dot{border-radius:50%;flex:none}

  /* Letterhead */
  .letterhead{position:absolute;left:90px;top:70px;width:640px;height:340px;background:var(--white);border-top:10px solid var(--glacier)}
  .letterhead .wordmark{position:absolute;left:26px;top:28px;color:var(--glacier);font-size:30px}
  .letterhead .wordmark .dot{width:28px;height:28px;border:6px solid var(--glacier)}
  .contact{font-size:12px;line-height:1.35}
  .contact .name{font-size:13px}
  .contact .role{font-size:8px;letter-spacing:.3px;margin-bottom:8px}
  .letterhead .contact{position:absolute;left:370px;top:24px;color:var(--ink)}

  /* Folder */
  .folder{position:absolute;left:770px;top:70px;width:340px;height:340px;background:linear-gradient(180deg,var(--glacier) 0%,var(--glacier-deep) 100%)}
  .folder .flap{position:absolute;left:0;top:0;width:100%;height:90px;background:linear-gradient(180deg,#4a4b4e,#38393b)}

  /* Cards */
  .card{position:absolute;overflow:hidden}
  .card.landscape{width:280px;height:170px;top:525px}
  .card.portrait{width:170px;height:280px;top:470px}
  .card .contact{position:absolute;left:18px;top:20px;color:var(--white)}
  .card .contact .role{margin-bottom:10px}
  .card.portrait .wordmark{position:absolute;left:18px;bottom:24px;color:var(--white);font-size:24px}
  .card.portrait .wordmark .dot{width:20px;height:20px;border:5px solid var(--white)}

  .card-blue-back{left:90px;background:var(--glacier)}
  .card-blue-front{left:410px;background:linear-gradient(160deg,var(--glacier) 0%,var(--glacier-deep) 100%)}
  .card-slate-front{left:620px;background:linear-gradient(160deg,var(--slate) 0%,var(--slate-deep) 100%)}
  .card-slate-back{left:830px;background:var(--slate)}

  .card .pattern{position:absolute;right:0;top:0;width:68%;height:100%;background:linear-gradient(135deg,var(--ice) 0%,var(--ice-shade) 100%)}
  .card.landscape .wordmark{position:absolute;left:104px;top:66px;font-size:28px;z-index:1}
  .card-blue-back .wordmark{color:var(--glacier)}
  .card-blue-back .wordmark .dot{width:32px;height:32px;background:var(--glacier)}
  .card-slate-back .wordmark{color:var(--slate)}
  .card-slate-back .wordmark .dot{width:32px;height:32px;background:var(--slate)}
</style>
</head>
<body>

<section class="letterhead">
  <div class="wordmark"><span class="dot"></span>Quorvix</div>
  <div class="contact">
    <div class="name">Elian Marsh</div>
    <div class="role">PRESIDENT</div>
    <div>Tallow Lane, 48</div>
    <div>+01 555 014 270</div>
    <div>+01 555 014 270</div>
    <div>elian@example-mail.com</div>
    <div>www.example-site.com</div>
  </div>
</section>

<section class="folder">
  <div class="flap" role="img" aria-label="Folder flap with faint repeating QUORVIX name pattern"></div>
</section>

<article class="card landscape card-blue-back">
  <div class="pattern" role="img" aria-label="Light triangle pattern with repeating QUORVIX lettering"></div>
  <div class="wordmark"><span class="dot"></span>Quorvix</div>
</article>

<article class="card portrait card-blue-front">
  <div class="contact">
    <div class="name">Elian Marsh</div>
    <div class="role">PRESIDENT</div>
    <div>Tallow Lane, 48</div>
    <div>+01 555 014 270</div>
    <div>+01 555 014 270</div>
    <div>elian@example-mail.com</div>
    <div>www.example-site.com</div>
  </div>
  <div class="wordmark"><span class="dot"></span>Quorvix</div>
</article>

<article class="card portrait card-slate-front">
  <div class="contact">
    <div class="name">Elian Marsh</div>
    <div class="role">PRESIDENT</div>
    <div>Tallow Lane, 48</div>
    <div>+01 555 014 270</div>
    <div>+01 555 014 270</div>
    <div>elian@example-mail.com</div>
    <div>www.example-site.com</div>
  </div>
  <div class="wordmark"><span class="dot"></span>Quorvix</div>
</article>

<article class="card landscape card-slate-back">
  <div class="pattern" role="img" aria-label="Light triangle pattern with repeating QUORVIX lettering"></div>
  <div class="wordmark"><span class="dot"></span>Quorvix</div>
</article>

</body>
</html>
```